Tech comm company needs a homepage banner

We need a banner for our homepage that inspires people about the possibilities of their written content. Taking the document to the next level. We need some beautiful imagery that evokes the idea that information can be "components" or blocks and connect to other assets... chatbots, Voice, other systems, A design that inspires the mind to think about the possibilities of information. Attached are some images. We have a corporate account w Ravok images, so please search that site.

1 page

```html
<!DOCTYPE html>
<html lang="en">
<head>
<meta charset="UTF-8">
<title>Homepage Banner</title>
<link href="https://fonts.googleapis.com/css2?family=Montserrat:wght@400;500;600;700&display=swap" rel="stylesheet">
<style>
  :root {
    --bg-deep: #221d74;
    --bg-mid: #33288f;
    --bg-light: #4a39b0;
    --accent: #2fb6ee;
    --text-light: #ffffff;
    --text-soft: #dcdaf2;
    --button-ink: #1e1968;
    --art-light: #b9b8f0;
    --art-mid: #7673d2;
    --art-dark: #3d3594;
  }
  html, body {
    margin: 0;
    padding: 0;
    width: 1200px;
    height: 531px;
    overflow: hidden;
  }
  .banner {
    position: relative;
    width: 1200px;
    height: 531px;
    overflow: hidden;
    background: linear-gradient(100deg, var(--bg-deep) 0%, var(--bg-mid) 50%, var(--bg-light) 100%);
    font-family: "Montserrat", sans-serif;
  }
  .hero-art {
    position: absolute;
    left: 600px;
    top: 0;
    width: 600px;
    height: 531px;
    background:
      radial-gradient(circle at 78% 42%, var(--art-light) 0%, var(--art-mid) 28%, var(--art-dark) 48%, rgba(61,53,148,0) 62%);
  }
  .hero-copy {
    position: absolute;
    left: 134px;
    top: 158px;
    width: 360px;
  }
  .hero-title {
    position: relative;
    margin: 0 0 24px 23px;
    color: var(--text-light);
    font-weight: 700;
    font-size: 32px;
    line-height: 41px;
    letter-spacing: -0.3px;
  }
  .hero-title::before {
    content: "";
    position: absolute;
    left: -23px;
    top: 6px;
    width: 5px;
    height: 36px;
    background: var(--accent);
  }
  .hero-text {
    margin: 0 0 25px;
    color: var(--text-soft);
    font-weight: 500;
    font-size: 12px;
    line-height: 19px;
    width: 350px;
  }
  .hero-actions {
    display: flex;
    gap: 10px;
    padding-left: 2px;
  }
  .button {
    box-sizing: border-box;
    width: 126px;
    height: 35px;
    display: flex;
    align-items: center;
    justify-content: center;
    font-family: "Montserrat", sans-serif;
    font-weight: 600;
    font-size: 11.5px;
    border-radius: 2px;
    text-decoration: none;
  }
  .button-primary {
    background: var(--text-light);
    color: var(--button-ink);
    box-shadow: 0 3px 8px rgba(10, 8, 50, 0.3);
  }
  .button-outline {
    border: 1.5px solid var(--accent);
    color: var(--accent);
  }
</style>
</head>
<body>
  <section class="banner">
    <div class="hero-art" role="img" aria-label="3D render of a faceted wireframe sphere with small floating polyhedron blocks in lavender and blue"></div>
    <div class="hero-copy">
      <h1 class="hero-title">Lorem ipsum dolor sit amet, adipise</h1>
      <p class="hero-text">Lorem ipsum dolor sit amet, consectetur adipiscing elit. Cras sit amet mi convallis, sodales lectus vel, molestie leo. Cras porttitor efficitur sapien ut ullamcorper.</p>
      <div class="hero-actions">
        <a class="button button-primary" href="#">Learn More</a>
        <a class="button button-outline" href="#">Get in Touch</a>
      </div>
    </div>
  </section>
</body>
</html>
```